Web design for sitter site

We will be launching a sitter site in the coming months that focuses on sitters for children. The name of this site will be KidHaven.com
We will need:
1. main page design
2. site logo designed
3. subpages as well for the look of people's profiles, and job listings, etc (see links below)
We only need the design, photos, font files, etc. We do not need this site coded (no html), a ps job is fine.
Some competing sites in the space include - tendlyhub.com and vurl.com
http://www.brisk-minder.example/images/profile1.jpg
http://quenthollibrary.example/wp-content/uploads/2013/09/vurl-review.png
http://www.palvermont.example/hr/photos/tendly_hub2.jpg
Target Market(s)
Mothers of children, mainly women
Industry/Entity Type
Online
Look and feel

```html
<!DOCTYPE html>
<html lang="en">
<head>
<meta charset="utf-8">
<title>KidHaven.com – Sign up</title>
<link rel="stylesheet" href="https://fonts.googleapis.com/css2?family=Arimo:wght@400;700&display=swap">
<style>
  :root {
    --plum: #6b1a45;
    --berry: #9c1e62;
    --rose: #c84a5e;
    --coral: #e05a3a;
    --caption: #cf5457;
    --peach: #fde3c8;
    --peach-hex: #fbd2b1;
    --field: #eef0f1;
    --panel: #faf7f7;
    --hero-bg: #f1f0f0;
    --white: #ffffff;
    --grey-text: #444444;
    --button: #c0392b;
  }
  * { box-sizing: border-box; margin: 0; padding: 0; }
  html, body { width: 1200px; height: 1120px; overflow: hidden; }
  body {
    position: relative;
    font-family: "Arimo", Arial, sans-serif;
    background: var(--white);
    color: var(--grey-text);
  }
  .abs { position: absolute; }

  /* Header */
  .site-header { position: absolute; left: 0; top: 0; width: 1200px; height: 120px; background: var(--white); }
  .brand-mark { left: 77px; top: 16px; width: 50px; height: 50px; border-radius: 50%;
    border: 4px solid var(--coral); }
  .brand { left: 39px; top: 80px; font-size: 24px; color: var(--plum); }
  .search { left: 492px; top: 40px; width: 193px; height: 34px; background: #eceef0; border-radius: 8px; }
  .search-label { left: 16px; top: 7px; font-size: 21px; color: #555; }
  .search-divider { left: 146px; top: 0; width: 1px; height: 34px; background: #d6d8da; }
  .search-icon { left: 160px; top: 7px; }
  .social { top: 48px; width: 24px; height: 24px; border-radius: 5px; }
  .social-a { left: 850px; background: #4c5ea3; }
  .social-b { left: 882px; background: #36a2dc; }
  .join-now { left: 932px; top: 40px; font-size: 22px; color: var(--plum); }
  .header-divider { left: 1042px; top: 34px; width: 2px; height: 40px; background: var(--plum); }
  .login { left: 1056px; top: 34px; width: 101px; height: 40px; border-radius: 8px;
    background: linear-gradient(#f4f4f4, #dedede); font-size: 23px; color: var(--plum);
    text-align: center; line-height: 40px; }

  /* Navigation */
  .main-nav { left: 0; top: 120px; width: 1200px; height: 66px;
    background: linear-gradient(90deg, var(--rose) 0%, #b84466 70%, var(--berry) 100%); }
  .nav-link { top: 19px; font-size: 23px; color: var(--white); }
  .nav-sep { top: 16px; width: 2px; height: 36px; background: rgba(255,255,255,0.75); }

  /* Hero */
  .hero { left: 0; top: 186px; width: 1200px; height: 315px; background: var(--hero-bg);
    box-shadow: 0 6px 10px rgba(0,0,0,0.12); }
  .hero-photo { left: 0; top: 0; width: 626px; height: 315px;
    background: linear-gradient(100deg, #e7c3ad 0%, #f3dccd 40%, #f7f1ee 75%, var(--hero-bg) 100%); }
  .signup-panel { left: 626px; top: 0; width: 482px; height: 315px; background: var(--panel); }
  .signup-title { left: 25px; top: 12px; font-size: 31px; color: var(--plum); }
  .signup-title strong { color: var(--coral); }
  .radio { top: 63px; width: 17px; height: 17px; border-radius: 50%; }
  .radio-on { left: 65px; background: var(--plum); border: 3px solid #e9d6df; }
  .radio-off { left: 226px; background: var(--white); border: 1px solid #ddd; }
  .radio-label { top: 61px; font-size: 19px; color: #333; }
  .field { height: 32px; background: var(--field); font-size: 18px; color: #333; padding: 5px 10px; }
  .checkbox { left: 243px; top: 200px; width: 28px; height: 28px; border-radius: 5px;
    background: #f3f3f3; border: 1px solid #ddd; }
  .terms { left: 280px; top: 208px; font-size: 12px; color: var(--button); }
  .join-button { left: 166px; top: 255px; width: 165px; height: 35px; border-radius: 6px;
    background: linear-gradient(#d9533d, var(--button)); color: var(--white); font-size: 15px;
    text-align: center; line-height: 35px; }

  /* How it works */
  .how-it-works { left: 0; top: 501px; width: 1200px; height: 422px; background: var(--peach); }
  .section-title { left: 0; top: 22px; width: 1200px; text-align: center; font-size: 30px;
    font-weight: 700; color: var(--coral); }
  .step-hex { top: 82px; width: 201px; height: 178px; }
  .step-icon { fill: none; stroke: var(--coral); stroke-width: 4; stroke-linecap: round; stroke-linejoin: round; }
  .step-arrow { top: 144px; }
  .step-caption { width: 320px; text-align: center; font-size: 27px; font-weight: 700;
    color: var(--caption); line-height: 34px; }

  /* Footer */
  .site-footer { left: 0; top: 923px; width: 1200px; height: 197px;
    background: linear-gradient(90deg, var(--rose) 0%, #b84466 70%, var(--berry) 100%); }
  .footer-link { top: 36px; font-size: 23px; color: var(--white); }
  .copyright { left: 0; top: 154px; width: 1354px; text-align: center; font-size: 22px; color: var(--white); }
</style>
</head>
<body>

<header class="site-header">
  <span class="abs brand-mark"></span>
  <div class="abs brand">KidHaven.com</div>
  <div class="abs search">
    <span class="abs search-label">Search</span>
    <span class="abs search-divider"></span>
    <svg class="abs search-icon" width="20" height="20" viewBox="0 0 20 20" aria-hidden="true">
      <circle cx="8" cy="8" r="5.5" fill="none" stroke="#555" stroke-width="2.2"/>
      <line x1="12" y1="12" x2="18" y2="18" stroke="#555" stroke-width="3" stroke-linecap="round"/>
    </svg>
  </div>
  <span class="abs social social-a" aria-label="Social profile"></span>
  <span class="abs social social-b" aria-label="Social profile"></span>
  <div class="abs join-now">Join now</div>
  <span class="abs header-divider"></span>
  <div class="abs login">Log in</div>
</header>

<nav class="abs main-nav">
  <span class="abs nav-link" style="left:269px">Home</span>
  <span class="abs nav-sep" style="left:362px"></span>
  <span class="abs nav-link" style="left:394px">About Us</span>
  <span class="abs nav-sep" style="left:518px"></span>
  <span class="abs nav-link" style="left:555px">Contact</span>
  <span class="abs nav-sep" style="left:676px"></span>
  <span class="abs nav-link" style="left:718px">Sitters</span>
  <span class="abs nav-sep" style="left:804px"></span>
  <span class="abs nav-link" style="left:829px">Parents</span>
  <span class="abs nav-sep" style="left:955px"></span>
</nav>

<section class="abs hero">
  <div class="abs hero-photo" role="img" aria-label="Photo of a mother kissing her smiling baby"></div>
  <form class="abs signup-panel">
    <div class="abs signup-title">Sign up for <strong>FREE!</strong></div>
    <span class="abs radio radio-on"></span>
    <span class="abs radio-label" style="left:95px">Parent</span>
    <span class="abs radio radio-off"></span>
    <span class="abs radio-label" style="left:258px">Sitter</span>
    <div class="abs field" style="left:25px;top:94px;width:416px">E- mail</div>
    <div class="abs field" style="left:25px;top:145px;width:189px">Password</div>
    <div class="abs field" style="left:240px;top:145px;width:201px">Confirm Password</div>
    <div class="abs field" style="left:25px;top:199px;width:189px">zip code</div>
    <span class="abs checkbox"></span>
    <span class="abs terms">I accept the terms of use</span>
    <div class="abs join-button">Join KidHaven.com</div>
  </form>
</section>

<section class="abs how-it-works">
  <h2 class="abs section-title">HOW IT WORKS</h2>

  <svg class="abs step-hex" style="left:134px" viewBox="0 0 201 178" role="img" aria-label="Computer screen icon: parents post jobs">
    <polygon points="50,0 151,0 201,89 151,178 50,178 0,89" fill="var(--peach-hex)"/>
    <g class="step-icon">
      <rect x="42" y="42" width="117" height="76" rx="4"/>
      <line x1="42" y1="106" x2="159" y2="106"/>
      <line x1="100" y1="118" x2="100" y2="134"/>
      <line x1="78" y1="136" x2="122" y2="136"/>
      <rect x="86" y="50" width="29" height="48"/>
      <line x1="92" y1="60" x2="109" y2="60"/>
      <line x1="92" y1="68" x2="109" y2="68"/>
      <line x1="92" y1="76" x2="109" y2="76"/>
      <line x1="92" y1="84" x2="109" y2="84"/>
    </g>
  </svg>
  <svg class="abs step-arrow" style="left:405px" width="28" height="40" viewBox="0 0 28 40" aria-hidden="true">
    <polyline points="4,6 22,20 4,34" fill="none" stroke="var(--caption)" stroke-width="4"/>
  </svg>
  <svg class="abs step-hex" style="left:477px" viewBox="0 0 201 178" role="img" aria-label="Group of sitters icon: sitters apply">
    <polygon points="50,0 151,0 201,89 151,178 50,178 0,89" fill="var(--peach-hex)"/>
    <g class="step-icon">
      <circle cx="62" cy="56" r="13"/>
      <path d="M36,112 V98 a26,26 0 0 1 52,0"/>
      <circle cx="139" cy="56" r="13"/>
      <path d="M113,98 a26,26 0 0 1 52,0 V112"/>
      <circle cx="100" cy="76" r="13"/>
      <path d="M74,136 V118 a26,26 0 0 1 52,0 V136"/>
    </g>
  </svg>
  <svg class="abs step-arrow" style="left:774px" width="28" height="40" viewBox="0 0 28 40" aria-hidden="true">
    <polyline points="4,6 22,20 4,34" fill="none" stroke="var(--caption)" stroke-width="4"/>
  </svg>
  <svg class="abs step-hex" style="left:846px" viewBox="0 0 201 178" role="img" aria-label="Handshake icon: the right match">
    <polygon points="50,0 151,0 201,89 151,178 50,178 0,89" fill="var(--peach-hex)"/>
    <g class="step-icon">
      <path d="M36,92 L68,60 L82,70"/>
      <path d="M165,86 L133,54 L104,62 L84,82 a8,8 0 0 0 12,12 L112,80"/>
      <path d="M112,80 L140,106 a8,8 0 0 1 -12,12 L114,104"/>
      <path d="M126,116 a8,8 0 0 1 -12,12 L102,116"/>
      <path d="M112,126 a8,8 0 0 1 -12,12 L54,108"/>
      <path d="M54,108 a8,8 0 0 1 10,-12"/>
      <path d="M64,118 a8,8 0 0 1 10,-12"/>
      <path d="M76,128 a8,8 0 0 1 10,-12"/>
    </g>
  </svg>

  <p class="abs step-caption" style="left:90px;top:302px">Parents post<br>jobs for sitters</p>
  <p class="abs step-caption" style="left:417px;top:293px">Sitters apply<br>for available jobs</p>
  <p class="abs step-caption" style="left:811px;top:302px">Everyone finds<br>the right match</p>
</section>

<footer class="abs site-footer">
  <span class="abs footer-link" style="left:40px">Home</span>
  <span class="abs footer-link" style="left:126px">About Us</span>
  <span class="abs footer-link" style="left:247px">Contact</span>
  <span class="abs footer-link" style="left:359px">Sitters</span>
  <span class="abs footer-link" style="left:451px">Parents</span>
  <div class="abs copyright">Copyright kidhaven.com 2014</div>
</footer>

</body>
</html>
```